Print Design for a Exhibition Booth

Hello,

Thanks for reading this requirement.

Our company is a global background screening company
www.velquarin.com

We have a portable exhibition booth which we exhibit in conferences. We need a new design which we need to print.

Please see attached following

1. Dimensions
2. Last design which we had ( backdrop + drape for table)
3. Actual image of what booth looks like with last design.

Design : We are looking for a design which is on similar lines.

please see attached some advertisement designs which we use in print. And also link to our corporate brochure.

Out put files should be in coreldraw open format.

Link to brochure : http://www.pagetrove.net/viewdoc.aspx?ID=48275190_213947

expectation : A print design for exhibt which is impactful.. gets eye balls. bright.. gives a global image ..

end caps : should have link of website www.velquarin.com

thanks

Target Market(s)

Business to Business

Industry/Entity Type

It Company

Font styles to use
Serif

Requirements
Must have
• should be impactful + bright colors + global look
• Out put files should be in coreldraw open format.

```html
<!DOCTYPE html>
<html lang="en">
<head>
<meta charset="utf-8">
<title>Velquarin Exhibition Booth – Backdrop and End Cap</title>
<link rel="stylesheet" href="https://fonts.googleapis.com/css2?family=Roboto+Condensed:wght@400;700&family=Tinos:wght@400;700&display=swap">
<style>
  :root {
    --stage: #000000;
    --sand-light: #f7e8c8;
    --sand: #f1dcb3;
    --sand-deep: #ecd3a4;
    --red: #e30613;
    --red-deep: #b5121b;
    --orange: #ef7d00;
    --green: #009a3e;
    --magenta: #e5007e;
    --navy: #1d4f91;
    --slate: #58595b;
    --ink: #1b1b1b;
    --shadow-band: #58585a;
    --white: #ffffff;
  }
  * { margin: 0; padding: 0; box-sizing: border-box; }
  html, body { width: 1200px; height: 934px; overflow: hidden; background: var(--stage); }
  .canvas { position: relative; width: 1200px; height: 934px; background: var(--stage); }

  .backdrop {
    position: absolute; left: 33px; top: 33px; width: 857px; height: 867px;
    background: linear-gradient(180deg, var(--sand-light) 0%, var(--sand) 55%, var(--sand-deep) 100%);
  }
  .backdrop__right {
    position: absolute; left: 447px; top: 0; width: 410px; height: 100%;
    background: linear-gradient(180deg, #f4e2c2 0%, #efd8ad 100%);
  }
  .ring {
    position: absolute; left: 75px; top: 90px; width: 370px; height: 370px; border-radius: 50%;
    background: conic-gradient(from 200deg, #f4e52a, #9fcf3a, #2fb59a, #2aa5c9, #63c0a8, #e6e032, #f4e52a);
    opacity: .85;
  }
  .ring__core {
    position: absolute; left: 52px; top: 52px; width: 266px; height: 266px; border-radius: 50%;
    background: var(--sand-light);
  }
  .ring__content { position: absolute; left: 157px; top: 225px; width: 190px; font-family: "Tinos", serif; }
  .brand-name { font-size: 25px; color: var(--navy); letter-spacing: .5px; line-height: 1; }
  .brand-tagline { font-size: 8.5px; color: var(--ink); line-height: 1.25; margin-top: 5px; }
  .service-list { list-style: none; text-align: right; margin-top: 6px; padding-right: 27px;
    font-family: "Roboto Condensed", sans-serif; font-size: 10px; color: var(--slate); line-height: 14.6px; }
  .service-list li:first-child { font-weight: 700; color: var(--ink); }

  .art { position: absolute; left: 0; top: 0; }
  .headline text, .endcap-headline text { font-family: "Roboto Condensed", sans-serif; font-weight: 700; }
  .ribbon-label { font-family: "Roboto Condensed", sans-serif; font-weight: 700; fill: var(--white); }

  .endcap {
    position: absolute; left: 910px; top: 67px; width: 255px; height: 833px;
    background: linear-gradient(180deg, var(--sand-light), var(--sand-deep));
  }
  .endcap__visual {
    position: absolute; left: 0; top: 0; width: 255px; height: 238px;
    background: linear-gradient(135deg, #f6ec9a 0%, #2aa5b8 22%, #6a3fa0 45%, #c2267a 62%, #ef8a1e 80%, #f5d36a 100%);
  }
  .endcap__brand { position: absolute; right: 12px; top: 200px; text-align: left; font-family: "Tinos", serif; }
  .endcap__brand-name { font-size: 13px; color: var(--navy); line-height: 1; }
  .endcap__brand-sub { font-family: "Roboto Condensed", sans-serif; font-size: 5.5px; color: var(--red-deep); letter-spacing: .3px; margin-top: 2px; }
  .endcap__web {
    position: absolute; left: 0; top: 719px; width: 255px; height: 34px; background: var(--navy);
    display: flex; align-items: center; gap: 8px; padding-left: 18px;
    font-family: "Roboto Condensed", sans-serif; font-weight: 700; font-size: 17px; color: var(--white);
  }
</style>
</head>
<body>
<div class="canvas">

  <section class="backdrop">
    <div class="backdrop__right"></div>
    <div class="ring" role="img" aria-label="Decorative flowing ring of fine lines in yellow, green and teal">
      <div class="ring__core"></div>
    </div>
    <div class="ring__content" style="left:124px;top:192px;">
      <div class="brand-name">VELQUARIN</div>
      <p class="brand-tagline">Your partner for BACKGROUND SCREENING in Asia and UAE</p>
      <ul class="service-list">
        <li>Background Checks</li>
        <li>Education Verification</li>
        <li>Employment Verification</li>
        <li>Professional License Checks</li>
        <li>Reference check</li>
        <li>Criminal Checks</li>
      </ul>
    </div>
  </section>

  <svg class="art" width="1200" height="934" viewBox="0 0 1200 934" aria-hidden="false">
    <g class="ribbon-shadows" fill="var(--shadow-band)">
      <polygon points="790,252 872,230 560,373 482,395"/>
      <polygon points="790,400 872,378 560,518 482,540"/>
      <polygon points="790,545 872,522 560,663 482,685"/>
      <polygon points="790,690 872,668 565,900 482,900"/>
    </g>
    <g class="ribbons">
      <polygon fill="var(--red)" points="490,245 872,137 872,230 490,335"/>
      <polygon fill="var(--orange)" points="482,395 872,283 872,378 482,485"/>
      <polygon fill="var(--green)" points="482,540 872,428 872,522 482,630"/>
      <polygon fill="var(--magenta)" points="482,685 872,573 872,668 482,775"/>
    </g>
    <g class="ribbon-label" text-anchor="middle">
      <text font-size="40" transform="translate(682,252) rotate(-15.8)">Background Checks</text>
      <text font-size="36" transform="translate(666,382) rotate(-15.8)">Business</text>
      <text font-size="36" transform="translate(672,422) rotate(-15.8)">Information Reports</text>
      <text font-size="36" transform="translate(668,528) rotate(-15.8)">Insurance Claims</text>
      <text font-size="36" transform="translate(662,568) rotate(-15.8)">Investigations</text>
      <text font-size="36" transform="translate(670,673) rotate(-15.8)">Assessments and</text>
      <text font-size="36" transform="translate(676,713) rotate(-15.8)">Online Services</text>
    </g>

    <g class="headline">
      <text x="65" y="585" font-size="68" fill="var(--red)" textLength="382" lengthAdjust="spacingAndGlyphs">MANAGE YOUR</text>
      <text x="65" y="655" font-size="64" fill="var(--navy)" textLength="240" lengthAdjust="spacingAndGlyphs">BUSINESS</text>
      <text x="320" y="655" font-size="64" fill="var(--red-deep)" textLength="127" lengthAdjust="spacingAndGlyphs">RISK,</text>
      <text x="65" y="740" font-size="76" fill="var(--slate)" textLength="315" lengthAdjust="spacingAndGlyphs">DIVERSITY</text>
      <text x="392" y="740" font-size="76" fill="var(--navy)" textLength="55" lengthAdjust="spacingAndGlyphs">&amp;</text>
      <text x="65" y="818" font-size="76" fill="var(--ink)" textLength="382" lengthAdjust="spacingAndGlyphs">COMPLIANCE</text>
    </g>
  </svg>

  <aside class="endcap">
    <div class="endcap__visual" role="img" aria-label="Colourful polygon network map linking Asian and Middle East countries"></div>
    <div class="endcap__brand">
      <div class="endcap__brand-name">VELQUARIN</div>
      <div class="endcap__brand-sub">RISK MANAGEMENT SERVICES</div>
    </div>
    <svg class="endcap-headline" width="255" height="700" viewBox="0 0 255 700" style="position:absolute;left:0;top:0;">
      <text x="18" y="378" font-size="92" fill="var(--red)" textLength="217" lengthAdjust="spacingAndGlyphs">YOUR</text>
      <text x="18" y="451" font-size="68" fill="var(--navy)" textLength="218" lengthAdjust="spacingAndGlyphs">GLOBAL</text>
      <text x="18" y="509" font-size="46" fill="var(--red-deep)" textLength="219" lengthAdjust="spacingAndGlyphs">BACKGROUND</text>
      <text x="18" y="569" font-size="46" fill="var(--slate)" textLength="219" lengthAdjust="spacingAndGlyphs">SCREENING</text>
      <text x="18" y="636" font-size="60" fill="var(--ink)" textLength="219" lengthAdjust="spacingAndGlyphs">PARTNER</text>
    </svg>
    <div class="endcap__web">
      <svg width="17" height="17" viewBox="0 0 20 20" aria-hidden="true">
        <circle cx="10" cy="10" r="9" fill="var(--white)"/>
        <g fill="none" stroke="var(--navy)" stroke-width="1.3">
          <ellipse cx="10" cy="10" rx="4" ry="9"/>
          <line x1="1" y1="10" x2="19" y2="10"/>
          <path d="M3 5.5h14M3 14.5h14"/>
        </g>
      </svg>
      <span>www.velquarin.com</span>
    </div>
  </aside>

</div>
</body>
</html>
```